Business Card

We would like a very clean corporate, two sided business card that conveys that we are a quality focused, reliable organisation that can make a business better. We focus on a cycle of continuous improvement for IT systems.

The brief is primarily clean and corporate, nothing overly complicated.

We sell IT services, IT support, server implementation, problem solving services to businesses in Australia.

Business

```html
<!DOCTYPE html>
<html lang="en">
<head>
<meta charset="utf-8">
<title>Tallis Core – Business Card</title>
<link href="https://fonts.googleapis.com/css2?family=Arimo:ital,wght@0,400;0,700;1,700&family=Open+Sans:wght@300&display=swap" rel="stylesheet">
<style>
  :root {
    --page: #ffffff;
    --card: #ffffff;
    --ink: #2a2d40;
    --brand-pink: #d6124f;
    --text: #222222;
    --shadow: rgba(0, 0, 0, 0.22);
  }
  * { margin: 0; padding: 0; box-sizing: border-box; }
  html, body {
    width: 1200px; height: 900px; overflow: hidden;
    background: var(--page);
    font-family: "Arimo", Arial, sans-serif;
  }
  .canvas { position: relative; width: 1200px; height: 900px; }
  .card {
    position: absolute;
    background: var(--card);
    box-shadow: 0 6px 18px var(--shadow);
  }
  .card--front { left: 344px; top: 48px; width: 520px; height: 346px; }
  .card--back { left: 334px; top: 496px; width: 540px; height: 354px; }

  .wordmark {
    position: absolute;
    display: flex; align-items: center; gap: 14px;
    font-family: "Arimo", Arial, sans-serif;
    font-weight: 700;
    color: var(--ink);
    line-height: 0.95;
    letter-spacing: -0.5px;
  }
  .wordmark__square { background: var(--brand-pink); flex: none; }
  .wordmark__name { display: flex; flex-direction: column; align-items: flex-end; }

  .card--front .wordmark { left: 36px; top: 108px; font-size: 60px; }
  .card--front .wordmark__square { width: 40px; height: 40px; }

  .card--back .wordmark { right: 40px; top: 14px; font-size: 34px; }
  .card--back .wordmark__square { width: 22px; height: 22px; }

  .tagline-band {
    position: absolute; right: 14px; top: 100px;
    width: 176px; height: 30px;
    background: var(--brand-pink);
    border-radius: 6px 0 0 0;
    color: #fff; font-size: 21px; line-height: 30px;
    padding-left: 14px;
  }
  .holder { position: absolute; left: 40px; top: 98px; }
  .holder__name {
    font-family: "Open Sans", Arial, sans-serif;
    font-weight: 300; font-size: 50px; color: var(--brand-pink);
    line-height: 1;
  }
  .holder__email {
    margin-left: 12px; margin-top: 12px;
    font-weight: 700; font-style: italic; font-size: 16px; color: var(--text);
  }
  .contact {
    position: absolute; right: 22px; top: 158px;
    font-style: normal;
    text-align: right; font-size: 14px; line-height: 20px; color: var(--text);
  }
  .contact__numbers { margin-top: 4px; }
  .web-band {
    position: absolute; right: 18px; bottom: 10px;
    width: 396px; height: 32px;
    background: var(--brand-pink);
    border-radius: 16px 0 0 0;
    color: #fff; font-size: 19px; line-height: 32px;
    text-align: center; letter-spacing: 6px;
  }
</style>
</head>
<body>
<main class="canvas">
  <section class="card card--front" aria-label="Card front">
    <div class="wordmark">
      <span class="wordmark__name"><span>tallis</span><span>core</span></span>
      <span class="wordmark__square"></span>
    </div>
  </section>

  <section class="card card--back" aria-label="Card back">
    <div class="wordmark">
      <span class="wordmark__name"><span>tallis</span><span>core</span></span>
      <span class="wordmark__square"></span>
    </div>
    <div class="tagline-band">IT Services</div>
    <div class="holder">
      <p class="holder__name">Name</p>
      <p class="holder__email">E-mail:</p>
    </div>
    <address class="contact">
      <p>Tallis Core Pty Ltd</p>
      <p>Suite 210, 14-18 Aster Lane</p>
      <p>Northbrook, NSW, 2100</p>
      <p>Australia</p>
      <div class="contact__numbers">
        <p>PH: +61 2 5550 1834</p>
        <p>FAX: +61 2 5550 1835</p>
        <p>ABN: 47 118 305 926</p>
      </div>
    </address>
    <div class="web-band">www.talliscore.net</div>
  </section>
</main>
</body>
</html>
```